Stationary & Business Card design for Solo Law Firm
stationary and business card design
Stationary & Business Card design for Solo Law Firm - Law
Creative Brief
Professional
Mira Dalton
Attorney at Law
317 W. Halverd Street, Suite 508 Colorado Springs, CO 80903
miradalton@kestrelpointlegal.example
kestrelpointlegal.example
underneath my logo I want the following to appear Family Law - Business - Trust & Estates (the spacing or symbol between these terms is up to you)
Logo on the back with the wording above underneath
quillmarsh quillmarsh
#98 can you make the text on the front vertical? and use the back from your #95 with the blue background. I like your submission #72 as well.
#134 can you make the text on the front go vertically instead of horizontally? also can you make the scales on the back bigger?
#141 on the front can you make it vertical? and on the back can you make the logo bigger and put the scales on the back?

```html
<!DOCTYPE html>
<html lang="en">
<head>
<meta charset="utf-8">
<title>Kestrel Point Legal — Business Card</title>
<link rel="stylesheet" href="https://fonts.googleapis.com/css2?family=Cinzel:wght@400;600&family=Cormorant+Garamond:wght@500&display=swap">
<style>
  :root {
    --backdrop: #8f8f8f;
    --rust: #bf6042;
    --paper: #ffffff;
    --ink-red: #b94a32;
    --line-blue: #1f4fa8;
    --cream: #fbeee6;
  }
  * { box-sizing: border-box; margin: 0; padding: 0; }
  html, body { width: 1200px; height: 908px; overflow: hidden; }
  body {
    background: var(--backdrop);
    display: flex;
    align-items: center;
    justify-content: center;
    gap: 40px;
  }
  .card {
    position: relative;
    width: 540px;
    height: 310px;
    border-radius: 18px;
    overflow: hidden;
  }
  .card--back {
    background: var(--rust);
    color: var(--cream);
    display: flex;
    flex-direction: column;
    align-items: center;
    justify-content: center;
    text-align: center;
  }
  .brand-name {
    font-family: "Cinzel", serif;
    font-weight: 600;
    font-size: 34px;
    letter-spacing: 1px;
  }
  .brand-rule {
    width: 250px;
    height: 1px;
    background: var(--cream);
    margin: 14px 0 12px;
  }
  .practice-areas {
    font-family: "Cinzel", serif;
    font-size: 14px;
    letter-spacing: 1.5px;
  }
  .card--front { background: var(--rust); }
  .front-shapes { position: absolute; inset: 0; }
  .front-brand {
    position: absolute;
    left: 30px;
    top: 52px;
    width: 240px;
    text-align: center;
  }
  .front-brand .brand-name { color: var(--ink-red); font-size: 24px; line-height: 1.25; }
  .front-brand .brand-rule { background: var(--line-blue); width: 200px; margin: 10px auto 0; }
  .holder {
    position: absolute;
    left: 36px;
    bottom: 24px;
    color: var(--cream);
    font-family: "Cinzel", serif;
    text-align: center;
    width: 200px;
  }
  .holder__name { font-size: 17px; letter-spacing: 1px; }
  .holder__title { font-size: 11px; letter-spacing: 1.5px; margin-top: 4px; }
  .contact {
    position: absolute;
    left: 318px;
    top: 150px;
    width: 210px;
    padding-left: 10px;
    border-left: 1px solid var(--cream);
    color: var(--cream);
    font-family: "Cormorant Garamond", serif;
    font-weight: 500;
    font-size: 11.5px;
    line-height: 1.45;
  }
  .contact li { list-style: none; white-space: nowrap; }
</style>
</head>
<body>
  <section class="card card--back">
    <div class="brand-name">Kestrel Point Legal</div>
    <div class="brand-rule"></div>
    <div class="practice-areas">Family Law · Business · Trust &amp; Estates</div>
  </section>

  <section class="card card--front">
    <svg class="front-shapes" viewBox="0 0 540 310" preserveAspectRatio="none">
      <path d="M0 0 H345 C330 120 250 210 0 240 Z" fill="var(--paper)"/>
      <path d="M345 0 C330 120 250 210 0 240" fill="none" stroke="var(--line-blue)" stroke-width="6"/>
    </svg>
    <div class="front-brand">
      <div class="brand-name">Kestrel Point Legal</div>
      <div class="brand-rule"></div>
    </div>
    <div class="holder">
      <div class="holder__name">Mira Dalton</div>
      <div class="holder__title">Attorney at Law</div>
    </div>
    <ul class="contact">
      <li>317 W. Halverd Street, Suite 508</li>
      <li>Colorado Springs, CO 80903</li>
      <li>(719) 555-0148</li>
      <li>miradalton@kestrelpointlegal.example</li>
      <li>kestrelpointlegal.example</li>
    </ul>
  </section>
</body>
</html>
```